Design cd cover for the vocal group: Ember, cd title Harbor Light. Cd cover is for EP release to be followed by full album. Songs are: Sizwe Langa Khona(Lift high the lamp); Cold River Road; Ngolwazi(Guide me through the night); When Rain Falls. There is no track entitled harbor light; the concept of the sound of gospel music as embodied in the music tracks - contemporary and traditional - is the basis of the album title.
NB: Project can close Tuesday 12 November to account for the 5 days as I do not count Saturday as a working day.
Hey guys,
Hello to everyone. I would like to take this opportunity to say thank you for your participation. Your submissions have been great and much appreciated. Forgive me for not being able to provide feedback to all of you. The time has come for me to make selection decisions and I would like to say thank you to all for your participation, you have been great and amazing.

```html
<!DOCTYPE html>
<html lang="en">
<head>
<meta charset="utf-8">
<title>Ember – Harbor Light EP Cover</title>
<link rel="stylesheet" href="https://fonts.googleapis.com/css2?family=Philosopher:wght@400;700&display=swap">
<style>
  :root {
    --sky-top: #5a5a86;
    --sky-rose: #c8607a;
    --sky-coral: #e0705e;
    --sky-amber: #e89a58;
    --ground: #070808;
    --track-text: #f3ede6;
    --copper: #c9784a;
    --title-text: #ffffff;
  }
  html, body {
    margin: 0;
    padding: 0;
    width: 1200px;
    height: 1200px;
    overflow: hidden;
    background: var(--ground);
  }
  .cover {
    position: relative;
    width: 1200px;
    height: 1200px;
    overflow: hidden;
    font-family: "Philosopher", sans-serif;
  }
  .cover__photo {
    position: absolute;
    inset: 0;
    background: linear-gradient(
      to bottom,
      var(--sky-top) 0%,
      var(--sky-rose) 28%,
      var(--sky-coral) 55%,
      var(--sky-amber) 78%,
      var(--ground) 92%,
      var(--ground) 100%
    );
  }
  .tracklist {
    position: absolute;
    left: 141px;
    top: 150px;
    margin: 0;
    padding: 0;
    list-style: none;
    color: var(--track-text);
    font-size: 40px;
    line-height: 55px;
    font-weight: 400;
  }
  .artist-mark {
    position: absolute;
    right: 110px;
    top: 880px;
    display: flex;
    flex-direction: column;
    align-items: flex-end;
  }
  .artist-mark__name {
    color: var(--copper);
    font-size: 150px;
    line-height: 1;
    font-weight: 400;
  }
  .release-title {
    margin-top: 14px;
    color: var(--title-text);
    font-size: 56px;
    line-height: 1;
    font-weight: 400;
  }
</style>
</head>
<body>
  <main class="cover">
    <div class="cover__photo" role="img" aria-label="Photograph of a pink and orange sunset sky over a dark hillside silhouette"></div>

    <ul class="tracklist">
      <li>Sizwe Langa Khona</li>
      <li>Cold River Road</li>
      <li>Ngolwazi</li>
      <li>When Rain Falls</li>
    </ul>

    <div class="artist-mark">
      <span class="artist-mark__name">Ember</span>
      <span class="release-title">Harbor Light</span>
    </div>
  </main>
</body>
</html>
```